Styling of small website for mid-sized Engineering and Manufacturing company

We need the styling for a professional website for a company wich delivers: engineering, manufacturing, assembling, servicing and prototyping. (typically, they produce complex devices in limited series (1-100 pieces. The client comes with an idea and they translate it into design and device).
We have already made a wire-frame, but need a style (colors, fonts, H1, H2, paragraphs, margins, padding etc).
The style must :
- express profession attitude (world of engineering)
- have a fresh, modern look
- be sober (enough (white) space between the elements
The style must also be able to be used in a RWD. At this moment the logo (just letters) uses a green color (#4C6E33), but it isn't an obligation to use the exact same color (even not the 'green' color itself if you think another color is better for the site).
Target Market(s)
engineering and production
Industry/Entity Type
It Company
Coding
Coded - Design and coding required
Number of Pages Required
5+ page

```html
<!DOCTYPE html>
<html lang="nl">
<head>
<meta charset="utf-8">
<title>Acme – Engineering &amp; Production</title>
<link href="https://fonts.googleapis.com/css2?family=Roboto:wght@400;500&display=swap" rel="stylesheet">
<style>
  :root{
    --green:#7dc123;
    --ink:#222222;
    --text:#555555;
    --band:#f8f8f8;
    --card-label:#2a2a2a;
    --footer:#2b2b2b;
    --footer-line:#3a3a3a;
    --white:#ffffff;
  }
  *{box-sizing:border-box;margin:0;padding:0}
  html,body{width:1168px;height:1200px;overflow:hidden;background:var(--white)}
  body{font-family:"Roboto",sans-serif;color:var(--text);position:relative}
  .wrap{width:798px;margin:0 auto;position:relative}

  .site-header{height:81px}
  .logo{position:absolute;left:0;top:14px;font-size:45px;font-weight:400;color:var(--ink);letter-spacing:1px}
  .main-nav{position:absolute;right:0;top:0;display:flex;height:81px;list-style:none}
  .main-nav li{font-size:11px;color:var(--ink);padding:0 15px;display:flex;align-items:center;text-transform:uppercase}
  .main-nav li:last-child{padding-right:0}
  .main-nav li.active{background:var(--green);color:var(--white);padding:0 14px;margin-right:5px}

  .intro{text-align:center;padding-top:40px}
  .intro h1{font-size:24px;font-weight:400;color:var(--green);margin-bottom:12px}
  .intro p{font-size:13.5px;line-height:21.7px;padding:0 0px}

  .works{position:absolute;left:0;top:261px;width:1168px;height:349px;background:var(--band)}
  .works h2{text-align:center;font-size:29px;font-weight:400;color:var(--ink);padding-top:42px;height:102px}
  .work-grid{display:flex;gap:23px}
  .work-card{width:182px}
  .work-photo{height:145px}
  .work-label{height:55px;background:var(--card-label);color:var(--white);font-size:16px;font-weight:500;display:flex;align-items:center;justify-content:center;letter-spacing:.3px}

  .summary{position:absolute;left:0;top:643px;width:1168px;text-align:center}
  .summary p{width:780px;margin:0 auto;font-size:13.5px;line-height:21.7px}

  .showcase{position:absolute;top:737px;left:185px;width:798px;height:240px}
  .section-title{font-size:16px;font-weight:400;color:var(--green);line-height:22px;text-transform:uppercase}
  .client-logo{position:absolute;left:0;top:39px;width:219px;height:165px;background:#f1f1f1;display:flex;align-items:center;justify-content:center;font-size:20px;font-weight:500;color:#1d4f7c}
  .client-text{position:absolute;left:241px;top:34px;width:315px;font-size:13.5px;line-height:21.8px}
  .why{position:absolute;left:599px;top:0;width:200px}
  .why ul{list-style:none;margin-top:6px}
  .why li{display:flex;align-items:center;height:26.6px;font-size:13.5px}
  .why li svg{margin-right:9px;flex:none}

  .site-footer{position:absolute;left:0;top:986px;width:1168px;height:214px;background:var(--footer);color:var(--white)}
  .footer-col{position:absolute;top:38px}
  .footer-col h3{font-size:16px;font-weight:400;text-transform:uppercase;margin-bottom:9px}
  .footer-col p{font-size:12.5px;line-height:20.5px}
  .map-btn{display:inline-flex;align-items:center;gap:6px;margin-top:10px;height:27px;width:95px;justify-content:center;background:#1e1e1e;border:1px solid #444;color:var(--white);font-size:11.5px;border-radius:2px}
  .copyright{position:absolute;left:0;bottom:0;width:100%;height:51px;border-top:1px solid var(--footer-line);display:flex;align-items:center;justify-content:center;font-size:11.5px}
</style>
</head>
<body>
  <header class="site-header wrap">
    <div class="logo">LOGO</div>
    <ul class="main-nav">
      <li class="active">Home</li>
      <li>Services</li>
      <li>Portfolio</li>
      <li>News</li>
      <li>About Acme</li>
      <li>Contact</li>
    </ul>
  </header>

  <section class="intro wrap">
    <h1>TECHNOLOGICAL SOLUTION IDEA TO PRODUCT</h1>
    <p>Acme ontwerpt en fabriceert to estellen voor de meest uniteenlopende industrieen. Met als belangrijkste de (para) medische sector. Onze Oplossingen zijn even veelzildig als de vragen van onze klanten. Engineering, prototype, (serie) productie en service onder een dak. Dat maakt het traject van vraag naar opplossing sneller en beter beheersbaar.</p>
  </section>

  <section class="works">
    <h2>OUR WORKS</h2>
    <div class="wrap work-grid">
      <div class="work-card">
        <div class="work-photo" role="img" aria-label="Engineers reviewing documents beside machinery in a workshop" style="background:linear-gradient(160deg,#cfd3cf,#7d7a70 60%,#3c4238)"></div>
        <div class="work-label">ENGINEERING</div>
      </div>
      <div class="work-card">
        <div class="work-photo" role="img" aria-label="Close-up of a milling machine cutting a metal part" style="background:linear-gradient(150deg,#e6e6e6,#5b6ea0 45%,#2a2e3a)"></div>
        <div class="work-label">PROTOTYPING</div>
      </div>
      <div class="work-card">
        <div class="work-photo" role="img" aria-label="Technician assembling a green machine on a production floor" style="background:linear-gradient(120deg,#3c6a2a,#8a8f7a 50%,#c9b540)"></div>
        <div class="work-label">ASSEMBLEREN</div>
      </div>
      <div class="work-card">
        <div class="work-photo" role="img" aria-label="Welder at work with sparks flying" style="background:linear-gradient(135deg,#c9a640,#3b4f8c 45%,#6c7fbf 75%,#2b2f48)"></div>
        <div class="work-label">SERVICING</div>
      </div>
    </div>
  </section>

  <section class="summary">
    <p>Van het eerste idee tot het kant-en-klare apparaat, volledig in eigen huis worden ontwikkeld. Engineering, Prototype, (serie) productie en service onder een dak. Dat maakt het traject van vraag naar oplossing sneller en beter beheersbaar.</p>
  </section>

  <section class="showcase">
    <h4 class="section-title">Showcase client X</h4>
    <div class="client-logo">Bluebrook Systems</div>
    <p class="client-text">Lorem ipsum dolor sit amet, consectetur adipiscing elit. Nulla quam velit, vulputate eu pharetra nec, mattis ac neque. Duis vulputate commodo lectus, ac blandit elit tincidunt id. Sed rhoncus, tortor sed eleifend tristique, tortor mauris molestie elit, et lacinia ipsum quam nec dui. Quisque nec mauric sit amet elit iaculis pretium sit amet quis magna. Aenean velit odio, elementum in tempus ut, vehicula eu diam.</p>
    <div class="why">
      <h4 class="section-title">Waarom klanten voor ons kiezen</h4>
      <ul>
        <li><svg width="11" height="11" viewBox="0 0 12 12"><circle cx="6" cy="6" r="6" fill="#7dc123"/><path d="M3.3 6.2l1.8 1.8 3.6-3.6" stroke="#fff" stroke-width="1.6" fill="none"/></svg>Al 4.251 abonnees</li>
        <li><svg width="11" height="11" viewBox="0 0 12 12"><circle cx="6" cy="6" r="6" fill="#7dc123"/><path d="M3.3 6.2l1.8 1.8 3.6-3.6" stroke="#fff" stroke-width="1.6" fill="none"/></svg>1 keer per maand</li>
        <li><svg width="11" height="11" viewBox="0 0 12 12"><circle cx="6" cy="6" r="6" fill="#7dc123"/><path d="M3.3 6.2l1.8 1.8 3.6-3.6" stroke="#fff" stroke-width="1.6" fill="none"/></svg>Exclusieve tips en promo’s</li>
        <li><svg width="11" height="11" viewBox="0 0 12 12"><circle cx="6" cy="6" r="6" fill="#7dc123"/><path d="M3.3 6.2l1.8 1.8 3.6-3.6" stroke="#fff" stroke-width="1.6" fill="none"/></svg>Al 4.251 abonnees</li>
        <li><svg width="11" height="11" viewBox="0 0 12 12"><circle cx="6" cy="6" r="6" fill="#7dc123"/><path d="M3.3 6.2l1.8 1.8 3.6-3.6" stroke="#fff" stroke-width="1.6" fill="none"/></svg>1 keer per maand</li>
        <li><svg width="11" height="11" viewBox="0 0 12 12"><circle cx="6" cy="6" r="6" fill="#7dc123"/><path d="M3.3 6.2l1.8 1.8 3.6-3.6" stroke="#fff" stroke-width="1.6" fill="none"/></svg>Exclusieve tips en promo’s</li>
      </ul>
    </div>
  </section>

  <footer class="site-footer">
    <div class="footer-col" style="left:185px">
      <h3>Contact us</h3>
      <p>Email: info@acmeworks.test<br>Phone: 0201234567</p>
    </div>
    <div class="footer-col" style="left:473px">
      <h3>Our slaes department</h3>
      <p>Street: xxx<br>xxx City</p>
      <div class="map-btn">View Map <svg width="20" height="12" viewBox="0 0 20 12"><path d="M1 1l5 5-5 5M9 1l5 5-5 5" stroke="#fff" stroke-width="2.4" fill="none"/></svg></div>
    </div>
    <div class="footer-col" style="left:815px">
      <h3>R&amp;D and production</h3>
      <p>Street: xxx<br>xxx City2</p>
      <div class="map-btn">View Map <svg width="20" height="12" viewBox="0 0 20 12"><path d="M1 1l5 5-5 5M9 1l5 5-5 5" stroke="#fff" stroke-width="2.4" fill="none"/></svg></div>
    </div>
    <div class="copyright">Copyright © 2015 ACME.com. All rights reserved</div>
  </footer>
</body>
</html>
```